Website for popular Robodroid App

We need a website for our popular Robodroid App "KOVU - Pocket Coder". KOVU is an App to make Apps:

https://apps.brimstore.example/details?id=com.kovu.app

We need the homepage design as well as the design for additional content pages. If possible post both designs when submitting.

On the homepage we would like to see the following elements:

- slogan + short description (exact wording tbd)

- logo (attached)

- embedded vidlane video http://vidlane.example/Qm7trPx2Kd and/or image showing mobile devices with app screenshots (attached)

- link to Brimstore: https://apps.brimstore.example/details?id=com.kovu.app

- link to Circlenet (should be highly visible): https://circlenet.example/558210937461102938475/posts

- less visible links to Chirplet & Friendwall

- statement: ">1000000 downloads"

- press coverage:

Gizmovex - http://www.gizmovex.example/2012/03/07/develop-android-using-kovu-video/
Robot Ledger - http://www.robotledger.example/2012/03/06/a-native-coder-lets-you-write-apps-on-your-tablet/
The Quillpost - http://www.quillpost.example/2012/03/13/mobile_kit/
Devlumo - http://www.devlumo.example/news/2012/03/KOVU/
Bytewharf - http://coders.bytewharf.example/story/12/03/14/8827410/beta-version-of-kovu-enables-app-building-on-phones

- user testimonials (taken from some 5 star Brimstore ratings)

- links to the content pages, e.g. "About us", "Features", "Getting started", "Community"

- anything else that comes to your mind

```html
<!DOCTYPE html>
<html lang="en">
<head>
<meta charset="utf-8">
<title>KOVU - Pocket Coder</title>
<link rel="stylesheet" href="https://fonts.googleapis.com/css2?family=Dosis:wght@500;600;700&family=PT+Sans:wght@400;700&family=Signika:wght@400;600&display=swap">
<style>
:root{
  --green:#6aa414;
  --green-dark:#4f8a0c;
  --green-light:#8fc51f;
  --cyan:#5dd6e4;
  --ink:#2b2b2b;
  --muted:#666;
  --link:#1a86c8;
  --line:#dcdcdc;
  --panel:#1f4a78;
  --panel-top:#333;
  --tint:#eefad8;
  --tint-line:#c8e3a3;
}
*{box-sizing:border-box;margin:0;padding:0}
html,body{width:1022px;height:1200px;overflow:hidden;background:#fff}
body{position:relative;font-family:"PT Sans",Arial,sans-serif;color:var(--ink);font-size:12px}
a{color:var(--link);text-decoration:none}
.abs{position:absolute}

/* header */
.site-header{left:0;top:0;width:1022px;height:98px;border-bottom:1px solid var(--line)}
.brand{left:89px;top:22px;display:flex;align-items:center;gap:10px;font-family:"Dosis",sans-serif;font-weight:700;font-size:30px;color:var(--cyan)}
.brand-mark{width:30px;height:30px;background:var(--green-light)}
.social{display:flex;gap:2px}
.social a{background:var(--cyan);color:#fff;font-family:"Dosis",sans-serif;font-weight:600;font-size:11px;height:35px;padding:0 8px;display:flex;align-items:center}
.social-top{right:88px;top:0}
.main-nav{left:406px;top:58px;display:flex;height:40px;border-top:1px solid var(--line)}
.main-nav a{font-family:"Dosis",sans-serif;font-weight:600;font-size:14px;color:#555;padding:0 11px;display:flex;align-items:center;border-right:1px solid var(--line);border-left:1px solid var(--line);margin-left:-1px}
.main-nav a.current{background:#e6e6e6;color:#555}

/* hero */
.hero{left:89px;top:115px;width:845px;height:346px;border:1px solid #d0d0d0;background:linear-gradient(#fbfbfb,#e4e4e4)}
.hero-art{left:14px;top:22px;width:480px;height:318px;border-radius:18px;background:linear-gradient(135deg,#3a3a3a,#111 60%,#cfcfcf)}
.hero-copy{left:506px;top:30px;width:320px}
.hero-copy h1{font-family:"Signika",sans-serif;font-weight:600;font-size:26px;line-height:27px;color:var(--green)}
.hero-copy p{margin-top:14px;font-size:11.5px;line-height:18px;color:#333;padding-left:4px}
.btn-download{left:510px;top:263px;width:146px;height:47px;border-radius:3px;background:linear-gradient(var(--green-light),var(--green-dark));display:flex;align-items:center;gap:10px;padding-left:14px;color:#fff;font-family:"Signika",sans-serif}
.btn-download .sq{width:22px;height:22px;background:#3d6e08}
.btn-download small{display:block;font-size:9px;color:#234800}
.btn-download b{font-size:15px;font-weight:600}

/* news */
.news{left:89px;top:479px;width:196px;height:283px;border:1px solid var(--line)}
.news h2,.video h2{font-family:"Dosis",sans-serif;font-weight:700;font-size:18px;color:#222}
.news h2{padding:8px 11px 6px;border-bottom:1px solid var(--line)}
.news ul{list-style:none;padding:8px 12px}
.news li{font-size:11px;line-height:13.5px;margin-bottom:9px;color:#333}
.news li a{display:block;word-break:break-all}
.downloads{left:89px;top:773px;width:196px;height:88px;background:linear-gradient(var(--green-light),var(--green-dark));color:#fff;font-family:"Signika",sans-serif;padding:10px 12px}
.downloads span{font-size:22px;display:block;line-height:22px}
.downloads strong{font-size:40px;font-weight:600;line-height:44px}

/* video */
.video{left:317px;top:487px;width:390px}
.video-frame{margin-top:10px;height:245px;background:#e4e4e4;padding:10px 9px}
.video-screen{position:relative;height:225px;background:linear-gradient(#111,#2a2a2a)}
.video-bar{position:absolute;left:0;right:0;bottom:16px;height:3px;background:#555}
.video-bar i{display:block;width:55px;height:3px;background:#d40000}
.video-controls{position:absolute;left:0;right:0;bottom:0;height:16px;background:#1b1b1b}
.video h3{margin-top:12px;font-size:12px;font-weight:700;color:#222}
.video p{font-size:11px;line-height:14px;color:var(--muted);margin-top:2px}

/* circlenet widget */
.feed{left:739px;top:479px;width:195px;height:307px;background:var(--panel)}
.feed-head{height:56px;background:var(--panel-top);display:flex;gap:8px;padding:8px 9px;color:#fff;font-size:11px;line-height:13px}
.feed-head .sq{flex:none;width:38px;height:38px;background:#fff;border:3px solid var(--cyan)}
.feed-head b{display:block;color:#4fb4f0;font-weight:400;font-size:12px}
.feed-body{padding:10px 22px 0 10px;color:#fff;font-size:11px;line-height:14px;position:relative;height:207px}
.feed-body .scroll{position:absolute;right:6px;top:4px;width:8px;height:195px;background:#fff}
.feed-body .scroll i{display:block;height:22px;background:#aaa}
.feed-body p{margin-bottom:8px}
.feed-body a{color:#6fc3ff}
.feed-body em{display:block;color:#6fc3ff;font-size:10.5px;margin-top:3px}
.feed-foot{height:44px;background:var(--panel-top);display:flex;align-items:center;gap:10px;padding:0 10px;color:#4fb4f0;font-size:10.5px;white-space:nowrap}
.feed-foot .sq{flex:none;width:20px;height:20px;background:#ddd}
.store{left:739px;top:796px;width:195px;height:65px;background:#000;border:1px solid #888;border-radius:6px;display:flex;align-items:center;justify-content:center;gap:10px;color:#fff;font-family:"PT Sans",sans-serif;font-size:26px}
.store .sq{width:24px;height:24px;background:#444}

/* testimonials */
.section-title{left:89px;top:886px;width:845px;display:flex;align-items:center;gap:12px;font-family:"Dosis",sans-serif;font-weight:700;font-size:17px;color:#222}
.section-title::before,.section-title::after{content:"";flex:1;height:1px;background:var(--line)}
.testimonials{left:89px;top:925px;width:845px;height:213px;background:var(--tint);border:1px solid var(--tint-line);display:flex}
.quote{flex:1;padding:23px 26px}
.quote+.quote{border-left:1px solid var(--tint-line)}
.quote p{font-size:11px;line-height:15.4px;color:#333}
.quote h4{margin-top:12px;font-family:"Signika",sans-serif;font-weight:400;font-size:14px;color:#222}
.stars{display:block;margin-top:6px}

/* footer */
.site-footer{left:89px;top:1165px;width:845px;border-top:1px solid var(--line);height:35px}
.site-footer p{position:absolute;left:0;top:11px;font-size:11px;color:#555}
.social-bottom{right:0;top:0}
</style>
</head>
<body>

<header class="site-header abs">
  <a class="brand abs" href="#"><span class="brand-mark"></span>KOVU</a>
  <nav class="social social-top abs"><a href="#">Friendwall</a><a href="#">Chirplet</a></nav>
  <nav class="main-nav abs">
    <a class="current" href="#">HOME</a><a href="#">ABOUT US</a><a href="#">FEATURES</a><a href="#">GETTING STARTED</a><a href="#">COMMUNITY</a><a href="#">CONTACT US</a>
  </nav>
</header>

<section class="hero abs">
  <div class="hero-art abs" role="img" aria-label="Tablet and phone showing the KOVU code editor and a running sample app"></div>
  <div class="hero-copy abs">
    <h1>Lorem ipsum dolor sit amet consectetur adipisicing elit</h1>
    <p>Sed ut perspiciatis unde omnis iste natus error sit voluptatem accusantium doloremque laudantium, totam rem aperiam, eaque ipsa quae ab illo inventore veritatis et quasi architecto beatae vitae dicta sunt explicabo. Nemo enim ipsam voluptatem quia voluptas sit aspernatur aut odit aut fugit, sed quia consequuntur magni dolores eos qui ratione voluptatem sequi nesciunt. Neque porro quisquam est, qui dolorem ipsum quia dolor sit amet, consectetur, adipisci velit.</p>
  </div>
  <a class="btn-download abs" href="#"><span class="sq"></span><span><small>Download now for</small><b>Robodroid</b></span></a>
</section>

<aside class="news abs">
  <h2>LATEST NEWS</h2>
  <ul>
    <li>Gizmovex -<a href="#">http://www.gizmovex.example/2012/03/07/develop-apps-using-kovu-video/</a></li>
    <li>Robot Ledger -<a href="#">http://www.gizmovex.example/2012/03/07/develop-apps-using-kovu-video/</a></li>
    <li>The Quillpost -<a href="#">http://www.quillpost.example/2012/03/13/mobile_kit/</a></li>
    <li>Devlumo -<a href="#">http://www.devlumo.example/news/2012/03/KOVU/</a></li>
  </ul>
</aside>
<div class="downloads abs"><span>Downloads</span><strong>1000000</strong></div>

<section class="video abs">
  <h2>WATCH OUR VIDEO</h2>
  <div class="video-frame">
    <div class="video-screen" role="img" aria-label="Video player showing KOVU creating a new app project">
      <div class="video-bar"><i></i></div>
      <div class="video-controls"></div>
    </div>
  </div>
  <h3>KOVU - Pocket Coder 2.0 on Nova Slate 2</h3>
  <p>A quick demo video creating, editing and running an App with the upcoming version 2.0 of KOVU on a Nova Slate 2.</p>
</section>

<aside class="feed abs">
  <div class="feed-head"><span class="sq"></span><div><b>KOVU - Pocket Coder</b>@ KOVU - Pocket Coder, Circlenet and web apps</div></div>
  <div class="feed-body">
    <div class="scroll"><i></i></div>
    <p>Reliving some memories of coding in my bedroom in my youth on a QX Vector hooked up to a TV thanks to +KOVU - Pocket... <a href="#">Viwe more</a><em>1 hour, 28 minutes ago</em></p>
    <p>Reliving some memories of coding in my bedroom in my youth on a QX Vector hooked up to a TV thanks to +KOVU - Pocket... <a href="#">Viwe more</a><em>1 hour, 28 minutes ago</em></p>
  </div>
  <div class="feed-foot"><span class="sq"></span>Get your Circlenet Feed widget!</div>
</aside>
<a class="store abs" href="#"><span class="sq"></span>Brimstore</a>

<h2 class="section-title abs">TESTIMONIALS</h2>
<section class="testimonials abs">
  <article class="quote">
    <p>This is Pixelforge's version of Lorem Ipsum. Proin gravida nibh vel velit auctor aliquet. Aenean sollicitudin, lorem quis bibendum auctor, nisi elit consequat ipsum, nec sagittis sem nibh id elit. Duis sed odio sit amet nibh vulputate cursus a sit amet mauris. Morbi accumsan ipsum velit. Nam nec tellus a odio tincidunt auctor a ornare odio. Sed non mauris vitae erat consequat auctor eu in elit. Class aptent taciti sociosqu ad litora torquent per conubia nostra, per inceptos himenaeos.</p>
    <h4>Jonas Ferrel</h4>
    <svg class="stars" width="74" height="13" viewBox="0 0 74 13" aria-label="1 of 5 stars"><path d="M6.5 0l1.9 4.2 4.6.4-3.5 3 1.1 4.5-4.1-2.4-4.1 2.4 1.1-4.5-3.5-3 4.6-.4z" fill="#4f8a0c"/><g fill="#c9c9c9"><path transform="translate(15 0)" d="M6.5 0l1.9 4.2 4.6.4-3.5 3 1.1 4.5-4.1-2.4-4.1 2.4 1.1-4.5-3.5-3 4.6-.4z"/><path transform="translate(30 0)" d="M6.5 0l1.9 4.2 4.6.4-3.5 3 1.1 4.5-4.1-2.4-4.1 2.4 1.1-4.5-3.5-3 4.6-.4z"/><path transform="translate(45 0)" d="M6.5 0l1.9 4.2 4.6.4-3.5 3 1.1 4.5-4.1-2.4-4.1 2.4 1.1-4.5-3.5-3 4.6-.4z"/><path transform="translate(60 0)" d="M6.5 0l1.9 4.2 4.6.4-3.5 3 1.1 4.5-4.1-2.4-4.1 2.4 1.1-4.5-3.5-3 4.6-.4z"/></g></svg>
  </article>
  <article class="quote">
    <p>This is Pixelforge's version of Lorem Ipsum. Proin gravida nibh vel velit auctor aliquet. Aenean sollicitudin, lorem quis bibendum auctor, nisi elit consequat ipsum, nec sagittis sem nibh id elit. Duis sed odio sit amet nibh vulputate cursus a sit amet mauris. Morbi accumsan ipsum velit. Nam nec tellus a odio tincidunt auctor a ornare odio. Sed non mauris vitae erat consequat auctor eu in elit. Class aptent taciti sociosqu ad litora torquent per conubia nostra, per inceptos himenaeos.</p>
    <h4>Jonas Ferrel</h4>
    <svg class="stars" width="74" height="13" viewBox="0 0 74 13" aria-label="1 of 5 stars"><path d="M6.5 0l1.9 4.2 4.6.4-3.5 3 1.1 4.5-4.1-2.4-4.1 2.4 1.1-4.5-3.5-3 4.6-.4z" fill="#4f8a0c"/><g fill="#c9c9c9"><path transform="translate(15 0)" d="M6.5 0l1.9 4.2 4.6.4-3.5 3 1.1 4.5-4.1-2.4-4.1 2.4 1.1-4.5-3.5-3 4.6-.4z"/><path transform="translate(30 0)" d="M6.5 0l1.9 4.2 4.6.4-3.5 3 1.1 4.5-4.1-2.4-4.1 2.4 1.1-4.5-3.5-3 4.6-.4z"/><path transform="translate(45 0)" d="M6.5 0l1.9 4.2 4.6.4-3.5 3 1.1 4.5-4.1-2.4-4.1 2.4 1.1-4.5-3.5-3 4.6-.4z"/><path transform="translate(60 0)" d="M6.5 0l1.9 4.2 4.6.4-3.5 3 1.1 4.5-4.1-2.4-4.1 2.4 1.1-4.5-3.5-3 4.6-.4z"/></g></svg>
  </article>
</section>

<footer class="site-footer abs">
  <p>Copyright © 2013 KOVU - Pocket Coder. All rights reserved</p>
  <nav class="social social-bottom abs"><a href="#">Friendwall</a><a href="#">Chirplet</a></nav>
</footer>

</body>
</html>
```